Business Card Design Project

Our logo/name is trademarked (since around 2000) and is owned by us. Logo originally designed in 1984 by my wife. Our logo needs freshening up while retaining its recognizability and trademark coverage. Our business cards, line card etc., web page home also need freshening, maybe as simple as inserting the updated logo, or completely redesigned.

Our logo represents "torque", which is defined as a force around an axis or "twist". Since 1949, we have been one of the world leaders in Norlane industrial clutches and brakes sales and service. We specialize in heavy duty applications such as stamping presses, steel mills, paper mills, drilling rigs etc. We are engineers as well as business people. Our customers are maintenance supervisors, plant engineers, small business owners. Our "color" has been reflex blue For more background, our website is www.brindlemark-co.com
Updates

I have posted a correct scan of the card/logo front and some previous versions of our logo.  (For now skip the back.)

As my brief said, we are after refreshing the logo and our cards/literature but the logo and card first.

Project Deadline Extended
Reason: I had trouble getting my existing logo scanned. should be up now.

Hopefully, the third try loading my existing logo and card worked!  The "City" banner had been on the0 bottom of the card.

Alt. A:  leave cities off
Alt B.  Instead of the cities, take a look at our web site home page or second page showing the world map and see if the world (as a territory which we do ship worldwide) could be worked in or highlight the back of the
 card with lines and the world? 

Future project will be line card redesign and web site
with separate project budget etc.www.brindlemark-co.com

Project Deadline Extended
Reason: My business partner was out of town last week and I wanted a couple days for his input. Thank you for your patience

Thank you all for your input! Dale Hurst

Target Market(s)

factory maintenance managers, plant engineers, small business owners

Industry/Entity Type

Small Business

Requirements
Must have
• clear development of existing trademarked logo

```html
<!DOCTYPE html>
<html lang="en">
<head>
<meta charset="utf-8">
<title>Brindlemark Business Card</title>
<link rel="stylesheet" href="https://fonts.googleapis.com/css2?family=Montserrat:wght@700;800&family=Questrial&display=swap">
<style>
  :root {
    --backdrop: #e4e5e7;
    --card: #ffffff;
    --card-shade: #f1f3f6;
    --reflex-blue: #0d4ea6;
    --band-light: #3f8fd6;
    --ink: #111111;
    --text: #1b1b1b;
    --title-blue: #1e64b8;
  }
  * { box-sizing: border-box; margin: 0; padding: 0; }
  html, body {
    width: 1200px;
    height: 800px;
    overflow: hidden;
    background: var(--backdrop);
  }
  .canvas {
    position: relative;
    width: 1200px;
    height: 800px;
  }
  .card {
    position: absolute;
    left: 150px;
    top: 143px;
    width: 900px;
    height: 514px;
    background: linear-gradient(170deg, var(--card) 0%, var(--card) 55%, var(--card-shade) 100%);
    box-shadow: 0 10px 30px rgba(0,0,0,0.18);
    overflow: hidden;
  }
  .card__band {
    position: absolute;
    left: 0;
    top: 0;
    width: 24px;
    height: 100%;
    background: var(--reflex-blue);
  }
  .card__band-cap {
    position: absolute;
    left: 0;
    top: 0;
    width: 24px;
    height: 44px;
    background: var(--band-light);
  }
  .brand {
    position: absolute;
    right: 62px;
    top: 78px;
    display: flex;
    align-items: center;
    gap: 16px;
  }
  .brand__name {
    font-family: "Montserrat", sans-serif;
    font-weight: 800;
    font-size: 46px;
    letter-spacing: 0.5px;
    color: var(--ink);
  }
  .brand__dot {
    width: 70px;
    height: 70px;
    border-radius: 50%;
    background: var(--reflex-blue);
  }
  .person {
    position: absolute;
    left: 78px;
    top: 306px;
  }
  .person__name {
    font-family: "Montserrat", sans-serif;
    font-weight: 700;
    font-size: 37px;
    color: var(--ink);
    line-height: 1.15;
  }
  .person__title {
    font-family: "Questrial", sans-serif;
    font-size: 33px;
    color: var(--title-blue);
    line-height: 1.3;
  }
  .contact {
    position: absolute;
    right: 58px;
    top: 304px;
    text-align: right;
    font-family: "Questrial", sans-serif;
    font-size: 21px;
    line-height: 30px;
    color: var(--text);
    list-style: none;
  }
  .contact__street { font-style: italic; }
</style>
</head>
<body>
<main class="canvas">
  <section class="card" aria-label="Business card for Dale Hurst, CEO of Brindlemark">
    <div class="card__band"></div>
    <div class="card__band-cap"></div>

    <div class="brand">
      <span class="brand__name">BRINDLEMARK</span>
      <span class="brand__dot"></span>
    </div>

    <div class="person">
      <p class="person__name">Dale Hurst</p>
      <p class="person__title">CEO</p>
    </div>

    <ul class="contact">
      <li class="contact__street">2280 N. Cedar Ridge Suite 240</li>
      <li>Ashford, MI 48317-2204</li>
      <li>(555) 214-3800</li>
      <li>Fax (555) 214-3817</li>
      <li>Parts Hotline (555) 390-4426</li>
      <li>dhurst@brindlemark-co.com</li>
    </ul>
  </section>
</main>
</body>
</html>
```